Harvest Gathering event flyer

I would like a church event flyer designed. The event is called "HARVEST GATHERING 2018". I am looking for a professional, yet catchy design that uses our brand colors and logo creatively while communicating key information of the event effectively.

1. The logo is attached in two color formats. The designer has the choice to use them as he/she want.

2. The location of the event is: Lindqvist Community Center, 482 Tamsworth Street, Portland, ME 04102
3. Time and date of event. The designer can organize and format the date and time as he/she pleases.
December 28th, 29th @ 7:00PM
December 30th @ 10:00AM
4. The topic of the event is "Tongues of fire". The designer is free to use this phrase as he/she pleases to create a good composition.
5. Speaker: Prophet Marcus Obuya
6. Contact information: contact@cedarbrookfellowship.org - Telephone number: 207 555 0148

7. I would also like the following three words on the flyer. These words describe the focus of the event: FIRE, REVIVAL, PROPHETIC

```html
<!DOCTYPE html>
<html lang="en">
<head>
<meta charset="utf-8">
<title>Harvest Gathering 2018 – Tongues of Fire</title>
<link rel="stylesheet" href="https://fonts.googleapis.com/css2?family=Lato:wght@300;400;700&family=Oswald:wght@300;400&family=Great+Vibes&display=swap">
<style>
  :root {
    --navy: #13365c;
    --orange: #f39a1e;
    --white: #ffffff;
    --mist: #e9eaee;
  }
  * { margin: 0; padding: 0; box-sizing: border-box; }
  html, body { width: 846px; height: 1200px; overflow: hidden; background: var(--mist); }
  .flyer {
    position: relative; width: 846px; height: 1200px; overflow: hidden;
    background: linear-gradient(180deg, #d9dbe2 0%, #eeeff2 60%, #e6e7eb 100%);
    font-family: 'Lato', sans-serif; color: var(--navy);
  }
  .sky {
    position: absolute; left: 0; top: 0; width: 846px; height: 760px;
    background:
      radial-gradient(circle at 20% 12%, rgba(243,154,30,.55), transparent 22%),
      radial-gradient(circle at 85% 40%, rgba(255,160,200,.45), transparent 25%),
      radial-gradient(circle at 10% 50%, rgba(47,127,140,.7), transparent 28%),
      radial-gradient(circle at 60% 55%, rgba(255,220,150,.55), transparent 22%),
      linear-gradient(180deg, #4a2d6a 0%, #6a4a8c 35%, #4d6f9a 62%, rgba(233,234,238,0) 100%);
  }
  .speaker-photo {
    position: absolute; left: 254px; top: 119px; width: 356px; height: 585px;
    background: linear-gradient(180deg, rgba(40,40,60,.55) 0%, rgba(30,60,130,.75) 45%, rgba(40,80,150,.35) 85%, rgba(233,234,238,0) 100%);
    border-radius: 40% 40% 8px 8px / 20% 20% 8px 8px;
  }
  .topic {
    position: absolute; top: 12px; left: 0; width: 100%; text-align: center;
    font-weight: 300; font-size: 34px; letter-spacing: 12px; color: var(--white);
  }
  .rule { position: absolute; height: 1px; background: var(--orange); }
  .pill {
    position: absolute; left: 220px; width: 418px; height: 36px; border-radius: 18px;
    background: var(--orange); color: var(--white); text-align: center; line-height: 36px;
  }
  .pill.speaker { top: 58px; font-size: 25px; }
  .pill.contact { top: 1091px; font-size: 20px; letter-spacing: 3px; }
  .event-title-script {
    position: absolute; left: 18px; top: 712px; font-family: 'Great Vibes', cursive;
    font-size: 172px; line-height: 1; color: var(--orange); white-space: nowrap;
  }
  .event-title-top {
    position: absolute; left: 350px; top: 740px; font-size: 54px; font-weight: 400; letter-spacing: 1px;
  }
  .event-year {
    position: absolute; left: 642px; top: 806px; font-family: 'Oswald', sans-serif; font-weight: 300;
    font-size: 64px; letter-spacing: 14px;
  }
  .focus {
    position: absolute; left: 366px; top: 892px; font-size: 27px; letter-spacing: 4px; font-weight: 400;
  }
  .schedule {
    position: absolute; left: 95px; top: 966px; width: 649px; height: 86px;
    border: 1px solid var(--navy); border-top: none;
  }
  .schedule svg { position: absolute; left: -6px; top: -4px; }
  .schedule-line {
    position: absolute; left: 0; width: 100%; text-align: center; white-space: nowrap;
    font-family: 'Oswald', sans-serif; font-weight: 300; font-size: 33px; transform: scaleX(.9);
  }
  .schedule-line.first { top: -8px; background: linear-gradient(90deg, transparent 22%, #eeeff2 22%, #eeeff2 78%, transparent 78%); }
  .schedule-line.second { top: 36px; }
  .venue {
    position: absolute; left: 0; top: 1060px; width: 100%; text-align: center;
    font-size: 15px; letter-spacing: 1.5px; font-weight: 400; white-space: nowrap;
  }
  .contact-row {
    position: absolute; top: 1144px; left: 0; width: 100%; height: 36px;
    font-family: 'Oswald', sans-serif; font-weight: 300; font-size: 20px; white-space: nowrap;
  }
  .contact-item { position: absolute; top: 0; height: 36px; display: flex; align-items: center; gap: 9px; }
  .contact-item.email { left: 110px; }
  .contact-item.phone { left: 492px; }
  .icon { flex: none; width: 34px; height: 34px; border-radius: 50%; background: var(--navy); display: flex; align-items: center; justify-content: center; }
  .brand-mark {
    position: absolute; left: 715px; top: 1119px; width: 120px; height: 72px; background: var(--navy);
    color: var(--white); font-size: 24px; font-weight: 400; letter-spacing: 1px;
    display: flex; align-items: center; justify-content: center;
  }
  .footer-band { position: absolute; left: 0; bottom: 0; width: 100%; height: 6px; background: var(--orange); }
</style>
</head>
<body>
<div class="flyer">
  <div class="sky" role="img" aria-label="Glowing bokeh lights and clouds in violet, teal and gold"></div>
  <div class="speaker-photo" role="img" aria-label="Photo of the speaker in a blue blazer holding a microphone and pointing forward"></div>

  <div class="topic">TONGUES OF FIRE</div>
  <div class="rule" style="left:100px;top:76px;width:120px"></div>
  <div class="rule" style="left:638px;top:76px;width:140px"></div>
  <div class="pill speaker">PROPHET MARCUS OBUYA</div>

  <div class="event-title-script">Gathering</div>
  <div class="event-title-top">HARVEST</div>
  <div class="event-year">2018</div>
  <div class="focus">FIRE, REVIVAL, PROPHETIC</div>

  <div class="schedule">
    <svg width="662" height="20" viewBox="0 0 662 20" aria-hidden="true">
      <line x1="6" y1="4" x2="656" y2="4" stroke="#13365c" stroke-width="1"/>
      <polygon points="0,0 26,0 0,22" fill="#f39a1e"/>
      <polygon points="662,0 636,0 662,22" fill="#f39a1e"/>
    </svg>
    <div class="schedule-line first">DECEMBER 28TH, 29TH @ 7:00PM</div>
    <div class="schedule-line second">DECEMBER 30TH @ 10:00AM</div>
  </div>

  <div class="venue">LINDQVIST COMMUNITY CENTER · 482 TAMSWORTH STREET, PORTLAND, ME 04102</div>

  <div class="rule" style="left:90px;top:1109px;width:130px"></div>
  <div class="rule" style="left:638px;top:1109px;width:126px"></div>
  <div class="pill contact">CONTACT INFORMATION</div>

  <div class="contact-row">
    <div class="contact-item email">
      <span class="icon">
        <svg width="18" height="13" viewBox="0 0 18 13" aria-hidden="true"><rect x="1" y="1" width="16" height="11" fill="none" stroke="#fff" stroke-width="1.4"/><polyline points="1,1 9,7 17,1" fill="none" stroke="#fff" stroke-width="1.4"/></svg>
      </span>
      <span>CONTACT@CEDARBROOKFELLOWSHIP.ORG</span>
    </div>
    <div class="contact-item phone">
      <span class="icon">
        <svg width="18" height="18" viewBox="0 0 24 24" aria-hidden="true"><path d="M6.6 10.8a15 15 0 0 0 6.6 6.6l2.2-2.2a1 1 0 0 1 1-.25 11.4 11.4 0 0 0 3.6.6 1 1 0 0 1 1 1V20a1 1 0 0 1-1 1A17 17 0 0 1 3 4a1 1 0 0 1 1-1h3.5a1 1 0 0 1 1 1c0 1.25.2 2.45.6 3.6a1 1 0 0 1-.25 1z" fill="none" stroke="#fff" stroke-width="1.6"/></svg>
      </span>
      <span>207 555 0148</span>
    </div>
  </div>

  <div class="brand-mark">BRAVEN</div>
  <div class="footer-band"></div>
</div>
</body>
</html>
```